BRASKETT LAND SERVICES BILLBOARD DESIGN

I NEED A BILLBOARD FOR MY BUSINESS. WE ARE A LAND CLEARING COMPANY AND I WOULD LIKE TO ADD A PICTURE OF MY TRACK LOADER TO THE SIGN. OPEN TO COLORS. I WOULD ALSO LIKE TO HAVE MY PHONE NUMBER 555-284-7196, WEBSITE WWW.BRASKETTLANDSERVICES.EXAMPLE, AND EMAIL ON THE SIGN (CONTACT@BRASKETTLANDSERVICES.EXAMPLE). DESIGNERS CAN HAVE THE FREEDOM TO DO WHATEVER STYLE THEY WANT AND TO USE ANY COLORS THEY WANT.

Target Market(s)

ANYONE WITH PROPERTY

Requirements
Must have
• PICTURE OF TRACK LOADER, WEBSITE, PHONE NUMBER, EMAIL
Nice to have
• OPEN TO ANYTHING
Should not have
• OPEN TO ANYTHING

```html
<!DOCTYPE html>
<html lang="en">
<head>
<meta charset="utf-8">
<title>Braskett Land Services Billboard</title>
<link href="https://fonts.googleapis.com/css2?family=Montserrat:wght@600;700;800&display=swap" rel="stylesheet">
<style>
  :root {
    --page-bg: #eef1f5;
    --board-blue: #1a5aa6;
    --band-dark: #15508f;
    --band-light: #1f66b8;
    --ink-white: #ffffff;
    --ink-navy: #14468f;
    --loader-orange: #e8641e;
    --loader-steel: #2b2e33;
  }
  html, body {
    margin: 0;
    width: 1200px;
    height: 962px;
    overflow: hidden;
    background: var(--page-bg);
    font-family: "Montserrat", Arial, sans-serif;
  }
  .billboard {
    position: absolute;
    left: 50px;
    top: 311px;
    width: 1100px;
    height: 340px;
    background: var(--board-blue);
    overflow: hidden;
    box-shadow: 0 10px 30px rgba(0,0,0,.18);
  }
  .billboard__bands {
    position: absolute;
    inset: 0;
  }
  .brand {
    position: absolute;
    left: 0;
    top: 28px;
    width: 470px;
    text-align: center;
    color: var(--ink-white);
    font-weight: 800;
    line-height: 1.02;
  }
  .brand__top { font-size: 50px; letter-spacing: 1px; }
  .brand__bottom { font-size: 50px; letter-spacing: 1px; }
  .phone-band {
    position: absolute;
    left: 30px;
    top: 160px;
    width: 440px;
    height: 72px;
    background: linear-gradient(90deg, rgba(255,255,255,.15) 0%, #ffffff 22%, #ffffff 65%, rgba(255,255,255,.2) 100%);
    display: flex;
    align-items: center;
    justify-content: center;
  }
  .phone-band__number {
    color: var(--ink-navy);
    font-weight: 800;
    font-size: 52px;
    letter-spacing: 1px;
  }
  .contact {
    position: absolute;
    left: 0;
    top: 248px;
    width: 470px;
    text-align: center;
    color: var(--ink-white);
    font-weight: 700;
    font-size: 18.5px;
    line-height: 1.55;
    text-transform: lowercase;
  }
  .loader-photo {
    position: absolute;
    left: 620px;
    top: 40px;
    width: 440px;
    height: 265px;
    border-radius: 6px;
    background:
      radial-gradient(ellipse at 62% 45%, var(--loader-orange) 0%, #c9541a 35%, rgba(43,46,51,.85) 70%, rgba(43,46,51,0) 100%);
  }
</style>
</head>
<body>
  <section class="billboard">
    <svg class="billboard__bands" viewBox="0 0 1100 340" preserveAspectRatio="none" aria-hidden="true">
      <polygon points="400,0 455,0 600,340 545,340" fill="var(--band-dark)"/>
      <polygon points="455,0 540,0 685,340 600,340" fill="var(--band-light)"/>
    </svg>

    <h1 class="brand">
      <span class="brand__top">BRASKETT</span><br>
      <span class="brand__bottom">LAND SERVICES</span>
    </h1>

    <div class="phone-band">
      <span class="phone-band__number">555-284-7196</span>
    </div>

    <div class="contact">
      <div class="contact__email">CONTACT@BRASKETTLANDSERVICES.EXAMPLE</div>
      <div class="contact__web">WWW.BRASKETTLANDSERVICES.EXAMPLE</div>
    </div>

    <div class="loader-photo" role="img" aria-label="Photo of an orange compact track loader with a toothed front bucket"></div>
  </section>
</body>
</html>
```